Create a Powerpoint presentation pack with our new logo

We have just selected a new logo using ArtHive and we were wanting to create a new Powerpoint presentation pack using this logo.
We'd like the powerpoint pack to have a title page + a header and footer page.
We would like the logo to appear on the title page and the header / footer page.
We are flexible with colours and want something that reflects an IT / travel flair.

I have attached the logo that we just selected from the arthive page.

Palomar Vista Systems is the IT division of Palomar Vista Journeys Group which is the largest travel retailer in Australia. We have offices in the US, Canada, UK, Singapore, Hong Kong, UAE, India, South Africa, Mexico and New Zealand.

```html
<!DOCTYPE html>
<html lang="en">
<head>
<meta charset="utf-8">
<title>Palomar Vista Systems – Presentation Pack</title>
<link href="https://fonts.googleapis.com/css2?family=Montserrat:wght@400;600;700;800&family=Open+Sans:wght@400;600&display=swap" rel="stylesheet">
<style>
:root{
  --red:#e3262d;
  --red-dark:#b81c22;
  --ink:#1d1d1f;
  --char:#2a2a2d;
  --coal:#3a3a3e;
  --grey:#8c8c90;
  --silver:#c9c9cc;
  --mist:#ececed;
  --paper:#ffffff;
}
*{box-sizing:border-box;margin:0;padding:0}
html,body{width:1200px;height:5019px;overflow:hidden;background:var(--paper)}
.deck{display:grid;grid-template-columns:repeat(3,392px);grid-auto-rows:220.5px;gap:8px;padding:0 4px}
.slide{position:relative;overflow:hidden;background:var(--paper);color:var(--ink);font-family:'Montserrat',sans-serif;box-shadow:inset 0 0 0 1px #e3e3e5}
.slide>*{position:absolute}
.slide.dark{background:var(--char);color:#fff;box-shadow:none}
.slide.black{background:#1a1a1c;color:#fff;box-shadow:none}
.std::after{content:"";position:absolute;right:10px;bottom:7px;width:7px;height:7px;border-radius:50%;background:var(--red)}
.title{left:16px;top:14px;font-size:9.5px;font-weight:700;letter-spacing:.3px;text-transform:uppercase}
.hero{font-size:17px;font-weight:700;line-height:1.1;text-transform:uppercase}
.sub{font:400 6px 'Open Sans',sans-serif;color:var(--silver)}
.copy{font:400 5px/1.55 'Open Sans',sans-serif;color:#6b6b70}
.dark .copy,.black .copy{color:#b9b9bd}
.copy strong{display:block;font:700 6px 'Montserrat',sans-serif;color:var(--ink);margin-bottom:2px}
.dark .copy strong,.black .copy strong,.on-red strong{color:#fff}
.on-red{color:#fff!important}
.logo{display:flex;align-items:center;gap:4px;font-weight:700;font-size:8px;letter-spacing:.6px;color:var(--red);white-space:nowrap}
.logo::before{content:"";width:7px;height:7px;border-radius:50%;background:currentColor}
.logo.light{color:#fff}
.photo{background:linear-gradient(135deg,#8b8f96,#4a4d53)}
.photo.sky{background:linear-gradient(160deg,#9fc3dd,#e9eef2 60%,#b9c6cf)}
.photo.dusk{background:linear-gradient(150deg,#5a5d64,#1f2023)}
.photo.sunset{background:linear-gradient(160deg,#f1b35a,#c9652a 55%,#3a2a22)}
.photo.office{background:linear-gradient(135deg,#cfcac4,#8e8882)}
.photo.beach{background:linear-gradient(180deg,#a8cde0,#e7dcc3 65%,#d1bf98)}
.photo.city{background:linear-gradient(180deg,#b6bcc4,#707780)}
.photo.mono{background:linear-gradient(135deg,#e4e4e6,#b3b3b7)}
.photo.round{border-radius:50%}
.box-red{background:var(--red);color:#fff}
.box-dark{background:var(--char);color:#fff}
.box-grey{background:var(--mist)}
.num{display:flex;align-items:center;justify-content:center;font-weight:700;font-size:9px;color:#fff}
.stat{font-size:15px;font-weight:700;line-height:1}
.rule{height:2px;background:var(--red)}
.track{height:3px;background:var(--mist)}
.track span{display:block;height:100%;background:var(--red)}
.list{display:flex;flex-direction:column;gap:9px}
.item{display:flex;gap:5px;align-items:flex-start}
.item i{flex:none;width:9px;height:9px;border-radius:50%;background:var(--red)}
.item i.k{background:var(--char)}
.item i.g{background:var(--grey)}
.item .copy{position:static}
.pill{font:600 5px 'Open Sans',sans-serif;display:flex;align-items:center;justify-content:center;text-align:center}
</style>
</head>
<body>
<main class="deck">

<!-- Row 1: title slides -->
<section class="slide black">
  <div class="photo dusk" role="img" aria-label="Dark sky backdrop" style="left:0;top:0;width:190px;height:221px"></div>
  <h1 class="hero" style="left:205px;top:86px">Your Title Here</h1>
  <p class="sub" style="left:206px;top:108px">Your subtitle goes here</p>
  <div class="logo light" style="left:206px;top:150px">PALOMAR VISTA</div>
</section>
<section class="slide black">
  <div class="photo sky" role="img" aria-label="Aircraft wing above the clouds at daylight" style="left:0;top:0;width:392px;height:221px;opacity:.9"></div>
  <h1 class="hero" style="left:180px;top:82px;color:#fff">Your Title Here</h1>
  <p class="sub" style="left:181px;top:104px;color:#fff">Your subtitle goes here</p>
  <div class="logo" style="left:181px;top:150px">PALOMAR VISTA</div>
</section>
<section class="slide">
  <div class="logo" style="left:22px;top:22px">PALOMAR VISTA</div>
  <h1 class="hero" style="left:22px;top:80px">Your Title Here</h1>
  <p class="sub" style="left:23px;top:102px;color:var(--grey)">Your subtitle goes here</p>
  <div class="photo mono" role="img" aria-label="Grey airliner taking off" style="left:250px;top:80px;width:120px;height:50px"></div>
</section>

<!-- Row 2 -->
<section class="slide dark">
  <div class="logo light" style="left:22px;top:60px">PALOMAR VISTA</div>
  <h1 class="hero" style="left:22px;top:96px">Your Title Here</h1>
  <p class="sub" style="left:23px;top:118px">Your subtitle goes here</p>
</section>
<section class="slide dark" style="background:#303034">
  <div class="photo dusk" role="img" aria-label="Dark aircraft backdrop" style="left:0;top:20px;width:150px;height:180px;opacity:.6"></div>
  <div class="logo light" style="left:160px;top:70px">PALOMAR VISTA</div>
  <h1 class="hero" style="left:160px;top:100px">Your Title Here</h1>
  <p class="sub" style="left:161px;top:122px">Your subtitle goes here</p>
</section>
<section class="slide dark">
  <div class="logo light" style="left:150px;top:62px">PALOMAR VISTA</div>
  <h1 class="hero" style="left:0;width:392px;text-align:center;top:100px">Your Title Goes Here</h1>
  <p class="sub" style="left:0;width:392px;text-align:center;top:122px">Your subtitle goes here</p>
</section>

<!-- Row 3 -->
<section class="slide std">
  <h2 class="title">Our Agenda</h2>
  <div class="num box-red" style="left:16px;top:48px;width:18px;height:18px">1</div>
  <p class="copy" style="left:40px;top:50px;width:140px"><strong>Agenda Title</strong>Short text about this point</p>
  <div class="num box-dark" style="left:16px;top:98px;width:18px;height:18px">2</div>
  <p class="copy" style="left:40px;top:100px;width:140px"><strong>Agenda Title</strong>Short text about this point</p>
  <div class="num box-red" style="left:16px;top:148px;width:18px;height:18px">3</div>
  <p class="copy" style="left:40px;top:150px;width:140px"><strong>Agenda Title</strong>Short text about this point</p>
  <div class="num box-dark" style="left:205px;top:48px;width:18px;height:18px">4</div>
  <p class="copy" style="left:229px;top:50px;width:140px"><strong>Agenda Title</strong>Short text about this point</p>
  <div class="num box-red" style="left:205px;top:98px;width:18px;height:18px">5</div>
  <p class="copy" style="left:229px;top:100px;width:140px"><strong>Agenda Title</strong>Short text about this point</p>
  <div class="num box-dark" style="left:205px;top:148px;width:18px;height:18px">6</div>
  <p class="copy" style="left:229px;top:150px;width:140px"><strong>Agenda Title</strong>Short text about this point</p>
</section>
<section class="slide std">
  <div class="photo office" role="img" aria-label="Hands typing on a laptop at a desk" style="left:0;top:0;width:196px;height:221px"></div>
  <div class="box-dark" style="left:196px;top:0;width:196px;height:221px"></div>
  <h2 class="title" style="left:212px;top:40px;color:#fff;line-height:1.3">Company<br>Featured<br>Product</h2>
  <p class="copy" style="left:212px;top:90px;width:160px">Write a short product summary here.</p>
  <div class="track" style="left:212px;top:120px;width:150px"><span style="width:78%"></span></div>
  <div class="track" style="left:212px;top:136px;width:150px"><span style="width:60%"></span></div>
  <div class="track" style="left:212px;top:152px;width:150px"><span style="width:88%"></span></div>
</section>
<section class="slide std">
  <h2 class="title">Bullets Point Level</h2>
  <div class="list" style="left:16px;top:46px;width:170px">
    <div class="item"><i></i><p class="copy"><strong>Your Text Here</strong>Short line of text</p></div>
    <div class="item"><i class="k"></i><p class="copy"><strong>Your Text Here</strong>Short line of text</p></div>
    <div class="item"><i></i><p class="copy"><strong>Your Text Here</strong>Short line of text</p></div>
    <div class="item"><i class="k"></i><p class="copy"><strong>Your Text Here</strong>Short line of text</p></div>
  </div>
  <div class="photo city" role="img" aria-label="Airport terminal interior" style="left:210px;top:46px;width:166px;height:140px"></div>
</section>

<!-- Row 4 -->
<section class="slide std">
  <div class="photo sky" role="img" aria-label="Sky and sea horizon" style="left:0;top:0;width:392px;height:120px"></div>
  <div class="box-dark" style="left:16px;top:20px;width:130px;height:70px"></div>
  <p class="copy" style="left:24px;top:30px;width:115px"><strong>Your Title Here</strong>Short text for this section</p>
  <div class="box-red" style="left:0;top:120px;width:392px;height:30px"></div>
  <p class="copy" style="left:16px;top:160px;width:170px">Add a short supporting paragraph here.</p>
  <p class="copy" style="left:206px;top:160px;width:170px">Add a short supporting paragraph here.</p>
</section>
<section class="slide std">
  <h2 class="title">Your Title Here</h2>
  <div class="box-dark" style="left:16px;top:50px;width:86px;height:100px"></div>
  <div class="box-red" style="left:106px;top:50px;width:86px;height:100px"></div>
  <div style="left:196px;top:50px;width:86px;height:100px;background:var(--grey)"></div>
  <div class="box-dark" style="left:286px;top:50px;width:90px;height:100px"></div>
  <p class="copy on-red" style="left:24px;top:110px;width:72px"><strong>Heading</strong>Short text</p>
  <p class="copy on-red" style="left:114px;top:110px;width:72px"><strong>Heading</strong>Short text</p>
  <p class="copy on-red" style="left:204px;top:110px;width:72px"><strong>Heading</strong>Short text</p>
  <p class="copy on-red" style="left:294px;top:110px;width:72px"><strong>Heading</strong>Short text</p>
</section>
<section class="slide std">
  <div style="left:0;top:108px;width:392px;height:1px;background:var(--silver)"></div>
  <div class="rule" style="left:230px;top:107px;width:60px"></div>
  <h2 class="hero" style="left:230px;top:118px;font-size:13px">Divider Page</h2>
</section>

<!-- Row 5 -->
<section class="slide std">
  <h2 class="title">Our Differences</h2>
  <div class="box-dark" style="left:16px;top:40px;width:180px;height:150px"></div>
  <div class="list" style="left:26px;top:52px;width:160px">
    <div class="item"><i></i><p class="copy">Short text about difference one</p></div>
    <div class="item"><i></i><p class="copy">Short text about difference two</p></div>
    <div class="item"><i></i><p class="copy">Short text about difference three</p></div>
    <div class="item"><i></i><p class="copy">Short text about difference four</p></div>
  </div>
  <div class="photo sky" role="img" aria-label="Sun rising behind clouds" style="left:206px;top:60px;width:170px;height:110px"></div>
</section>
<section class="slide std">
  <h2 class="title">Text &amp; Bullet Area</h2>
  <p class="copy" style="left:16px;top:46px;width:130px"><strong style="color:var(--red)">Heading Here</strong>Write a short paragraph of supporting text for this area.</p>
  <div class="list" style="left:170px;top:46px;width:100px">
    <div class="item"><i></i><p class="copy">Your Text Here</p></div>
    <div class="item"><i class="k"></i><p class="copy">Your Text Here</p></div>
    <div class="item"><i></i><p class="copy">Your Text Here</p></div>
    <div class="item"><i class="k"></i><p class="copy">Your Text Here</p></div>
  </div>
  <div class="list" style="left:280px;top:46px;width:100px">
    <div class="item"><i class="g"></i><p class="copy">Your Text Here</p></div>
    <div class="item"><i class="g"></i><p class="copy">Your Text Here</p></div>
    <div class="item"><i class="g"></i><p class="copy">Your Text Here</p></div>
    <div class="item"><i class="g"></i><p class="copy">Your Text Here</p></div>
  </div>
</section>
<section class="slide std">
  <div class="box-grey" style="left:20px;top:24px;width:80px;height:34px"></div>
  <div class="box-grey" style="left:20px;top:92px;width:80px;height:34px"></div>
  <div class="box-grey" style="left:20px;top:160px;width:80px;height:34px"></div>
  <div class="box-grey" style="left:292px;top:24px;width:80px;height:34px"></div>
  <div class="box-grey" style="left:292px;top:92px;width:80px;height:34px"></div>
  <div class="box-grey" style="left:292px;top:160px;width:80px;height:34px"></div>
  <div class="box-dark pill" style="left:120px;top:90px;width:152px;height:40px;font:700 10px 'Montserrat',sans-serif">OUR AWESOME CLIENT</div>
</section>

<!-- Row 6 -->
<section class="slide dark">
  <div style="left:0;top:0;width:392px;height:221px;display:flex">
    <div style="flex:1;border-right:1px solid #444"></div><div style="flex:1;border-right:1px solid #444"></div><div style="flex:1;border-right:1px solid #444"></div><div style="flex:1;border-right:1px solid #444"></div><div style="flex:1;background:var(--red)"></div>
  </div>
  <svg style="left:0;top:70px" width="392" height="24" viewBox="0 0 392 24">
    <g fill="none" stroke="#fff" stroke-width="1.4">
      <rect x="31" y="4" width="16" height="14" rx="2"/><circle cx="117" cy="11" r="7"/><path d="M187 18l8-14 8 14z"/><circle cx="274" cy="10" r="6"/><path d="M278 14l5 5"/><rect x="345" y="5" width="16" height="12"/>
    </g>
  </svg>
  <p class="copy" style="left:8px;top:110px;width:62px;text-align:center"><strong>Heading</strong>Short text</p>
  <p class="copy" style="left:86px;top:110px;width:62px;text-align:center"><strong>Heading</strong>Short text</p>
  <p class="copy" style="left:165px;top:110px;width:62px;text-align:center"><strong>Heading</strong>Short text</p>
  <p class="copy" style="left:243px;top:110px;width:62px;text-align:center"><strong>Heading</strong>Short text</p>
  <p class="copy on-red" style="left:322px;top:110px;width:62px;text-align:center"><strong>Heading</strong>Short text</p>
</section>
<section class="slide std">
  <h2 class="title">Our Mockup Area</h2>
  <div style="left:110px;top:38px;width:170px;height:110px;background:#2b2b2e;border:5px solid #3a3a3e"></div>
  <div class="logo light" style="left:150px;top:86px">PALOMAR VISTA</div>
  <div style="left:180px;top:150px;width:30px;height:14px;background:var(--silver)"></div>
  <p class="copy" style="left:16px;top:176px;width:360px;text-align:center">Add a short description of your product here.</p>
</section>
<section class="slide dark">
  <div class="photo dusk" role="img" aria-label="Dark picture placeholder" style="left:0;top:0;width:150px;height:221px"></div>
  <h2 class="hero" style="left:40px;top:88px;font-size:12px">Picture<br>Slide</h2>
  <div style="left:150px;top:0;width:242px;height:221px;background:#fff"></div>
  <svg style="left:170px;top:30px" width="200" height="110" viewBox="0 0 200 110">
    <g fill="#2a2a2d"><rect x="10" y="40" width="14" height="70"/><rect x="58" y="20" width="14" height="90"/><rect x="106" y="50" width="14" height="60"/><rect x="154" y="30" width="14" height="80"/></g>
    <g fill="#e3262d"><rect x="26" y="60" width="14" height="50"/><rect x="74" y="45" width="14" height="65"/><rect x="122" y="30" width="14" height="80"/><rect x="170" y="10" width="14" height="100"/></g>
  </svg>
  <div class="stat" style="left:170px;top:160px;color:var(--ink)"><span style="color:var(--red)">★</span> 85%</div>
  <p class="copy" style="left:240px;top:163px;width:130px">Short text about this figure</p>
</section>

<!-- Row 7 -->
<section class="slide std">
  <div class="rule" style="left:20px;top:120px;width:50px"></div>
  <h2 class="hero" style="left:20px;top:130px;font-size:13px">Divider Page</h2>
  <p class="sub" style="left:20px;top:150px;color:var(--grey)">Your subtitle here</p>
</section>
<section class="slide std">
  <div class="box-dark" style="left:0;top:0;width:150px;height:221px"></div>
  <h2 class="title" style="color:#fff">Our Mockup Area</h2>
  <div class="list" style="left:16px;top:50px;width:120px">
    <div class="item"><i></i><p class="copy">Your text here</p></div>
    <div class="item"><i></i><p class="copy">Your text here</p></div>
    <div class="item"><i></i><p class="copy">Your text here</p></div>
  </div>
  <div style="left:180px;top:40px;width:180px;height:116px;background:#fff;border:5px solid #2b2b2e"></div>
  <div class="logo" style="left:230px;top:92px">PALOMAR VISTA</div>
  <div class="box-dark" style="left:255px;top:158px;width:30px;height:14px"></div>
</section>
<section class="slide std">
  <h2 class="hero" style="left:16px;top:40px;font-size:12px">This Is Line<br>Chart Slide</h2>
  <p class="copy" style="left:16px;top:80px;width:110px">Short text describing the chart trend.</p>
  <svg style="left:140px;top:30px" width="240" height="150" viewBox="0 0 240 150">
    <g stroke="#e5e5e7"><line x1="0" y1="30" x2="240" y2="30"/><line x1="0" y1="70" x2="240" y2="70"/><line x1="0" y1="110" x2="240" y2="110"/><line x1="0" y1="149" x2="240" y2="149"/></g>
    <polyline points="0,100 50,60 100,110 150,30 200,80 240,50" fill="none" stroke="#e3262d" stroke-width="2"/>
    <polyline points="0,120 50,90 100,70 150,100 200,60 240,90" fill="none" stroke="#2a2a2d" stroke-width="2"/>
  </svg>
</section>

<!-- Row 8 -->
<section class="slide std">
  <h2 class="title">Your Title Goes Here</h2>
  <div class="photo office" role="img" aria-label="Business meeting" style="left:16px;top:40px;width:110px;height:70px"></div>
  <div class="box-dark" style="left:130px;top:40px;width:110px;height:70px"></div>
  <div class="box-red" style="left:16px;top:114px;width:110px;height:70px"></div>
  <div class="photo city" role="img" aria-label="Laptop on a desk" style="left:130px;top:114px;width:110px;height:70px"></div>
  <p class="copy" style="left:138px;top:60px;width:95px"><strong>Heading Here</strong>Short text</p>
  <p class="copy on-red" style="left:24px;top:134px;width:95px"><strong>Heading Here</strong>Short text</p>
  <p class="copy" style="left:256px;top:44px;width:120px">Add a short paragraph of supporting text for this slide here.</p>
</section>
<section class="slide std">
  <div class="photo office" role="img" aria-label="Person working at a laptop" style="left:0;top:0;width:392px;height:221px"></div>
  <div class="box-dark" style="left:196px;top:30px;width:170px;height:150px;opacity:.92"></div>
  <h2 class="title" style="left:210px;top:44px;color:#fff">About Us</h2>
  <p class="copy" style="left:210px;top:64px;width:145px">Write a short introduction to the team and what it does.</p>
</section>
<section class="slide dark">
  <div class="photo dusk" role="img" aria-label="Airliner tail on a dark sky" style="left:0;top:0;width:392px;height:221px"></div>
  <div class="logo light" style="left:20px;top:20px">PALOMAR VISTA</div>
  <h2 class="hero" style="left:20px;top:150px;font-size:13px">This Is Your Divider Page</h2>
</section>

<!-- Row 9 -->
<section class="slide std">
  <h2 class="title">Quote Area</h2>
  <p class="copy" style="left:16px;top:46px;width:130px;font-size:6px;color:var(--ink)">“Coming together is a beginning, working together is success.”</p>
  <p class="copy" style="left:16px;top:90px;color:var(--red)">– Quote Author</p>
  <div class="photo sunset" role="img" aria-label="Airliner flying across a sunset" style="left:160px;top:0;width:232px;height:221px"></div>
</section>
<section class="slide std">
  <h2 class="title">Brand Detailed</h2>
  <div class="photo office" role="img" aria-label="Laptop and coffee on a desk" style="left:16px;top:40px;width:170px;height:120px"></div>
  <div class="box-red" style="left:186px;top:60px;width:110px;height:80px"></div>
  <p class="copy on-red" style="left:196px;top:72px;width:90px"><strong>Brand Title</strong>Short text here</p>
  <p class="copy" style="left:306px;top:60px;width:74px">Add a short line of text here.</p>
</section>
<section class="slide std">
  <h2 class="title">Product Philosophy</h2>
  <svg style="left:151px;top:55px" width="90" height="90" viewBox="0 0 90 90">
    <circle cx="45" cy="45" r="34" fill="none" stroke="#2a2a2d" stroke-width="18"/>
    <circle cx="45" cy="45" r="34" fill="none" stroke="#e3262d" stroke-width="18" stroke-dasharray="110 214" transform="rotate(-90 45 45)"/>
    <circle cx="45" cy="45" r="34" fill="none" stroke="#c9c9cc" stroke-width="18" stroke-dasharray="50 214" stroke-dashoffset="-110" transform="rotate(-90 45 45)"/>
  </svg>
  <p class="copy" style="left:16px;top:60px;width:120px"><strong>Heading Here</strong>Short line of text</p>
  <p class="copy" style="left:16px;top:120px;width:120px"><strong>Heading Here</strong>Short line of text</p>
  <p class="copy" style="left:258px;top:60px;width:120px"><strong>Heading Here</strong>Short line of text</p>
  <p class="copy" style="left:258px;top:120px;width:120px"><strong>Heading Here</strong>Short line of text</p>
</section>

<!-- Row 10 -->
<section class="slide std">
  <div class="photo city" role="img" aria-label="City skyline" style="left:0;top:0;width:392px;height:60px;opacity:.5"></div>
  <svg style="left:16px;top:70px" width="360" height="110" viewBox="0 0 360 110">
    <g fill="#e3262d"><rect x="10" y="30" width="22" height="80"/><rect x="100" y="10" width="22" height="100"/><rect x="190" y="50" width="22" height="60"/><rect x="280" y="20" width="22" height="90"/></g>
    <g fill="#2a2a2d"><rect x="36" y="50" width="22" height="60"/><rect x="126" y="40" width="22" height="70"/><rect x="216" y="30" width="22" height="80"/><rect x="306" y="60" width="22" height="50"/></g>
  </svg>
  <p class="copy" style="left:26px;top:186px">Item One</p><p class="copy" style="left:116px;top:186px">Item Two</p><p class="copy" style="left:206px;top:186px">Item Three</p><p class="copy" style="left:296px;top:186px">Item Four</p>
</section>
<section class="slide std">
  <h2 class="title">Trending in the World</h2>
  <div class="photo mono" role="img" aria-label="Grey world map" style="left:16px;top:40px;width:240px;height:130px"></div>
  <div class="num" style="left:60px;top:80px;width:26px;height:26px;border-radius:50%;background:var(--coal);font-size:6px">80%</div>
  <div class="num" style="left:150px;top:100px;width:26px;height:26px;border-radius:50%;background:var(--red);font-size:6px">65%</div>
  <div class="list" style="left:270px;top:50px;width:110px">
    <div class="item"><i></i><p class="copy">Your text here</p></div>
    <div class="item"><i class="k"></i><p class="copy">Your text here</p></div>
    <div class="item"><i></i><p class="copy">Your text here</p></div>
  </div>
</section>
<section class="slide dark">
  <h2 class="title">Our Vision &amp; Mission</h2>
  <div class="photo dusk" role="img" aria-label="Dark city skyline" style="left:0;top:120px;width:392px;height:101px;opacity:.6"></div>
  <p class="copy" style="left:16px;top:46px;width:160px"><strong><span style="color:var(--red)">●</span> Our Vision</strong>Go to the next level without limit in the world.</p>
  <p class="copy" style="left:206px;top:46px;width:170px"><strong><span style="color:var(--red)">●</span> Our Missions</strong>Your text here<br>Your text here<br>Your text here</p>
</section>

<!-- Row 11 -->
<section class="slide std">
  <h2 class="title">Our Services</h2>
  <div class="photo sky" role="img" aria-label="Airliner taking off" style="left:16px;top:40px;width:170px;height:90px"></div>
  <p class="copy" style="left:16px;top:140px;width:170px"><strong style="color:var(--red)">Your Title Here</strong>Short description of this service.</p>
  <div class="list" style="left:206px;top:44px;width:170px">
    <div class="item"><i></i><p class="copy"><strong>Service One</strong>Short text</p></div>
    <div class="item"><i class="k"></i><p class="copy"><strong>Service Two</strong>Short text</p></div>
    <div class="item"><i></i><p class="copy"><strong>Service Three</strong>Short text</p></div>
  </div>
</section>
<section class="slide std">
  <h2 class="title">Three Column Description</h2>
  <p class="copy" style="left:16px;top:40px;width:360px;color:var(--red);font-size:6px">This is a place for your headline text that you want your audience to read.</p>
  <p class="copy" style="left:16px;top:70px;width:110px">Write a short paragraph of supporting text in this column.</p>
  <p class="copy" style="left:141px;top:70px;width:110px">Write a short paragraph of supporting text in this column.</p>
  <p class="copy" style="left:266px;top:70px;width:110px">Write a short paragraph of supporting text in this column.</p>
</section>
<section class="slide std">
  <h2 class="title">Our Team</h2>
  <div class="photo office round" role="img" aria-label="Team member portrait" style="left:166px;top:40px;width:60px;height:60px"></div>
  <p class="copy" style="left:96px;top:110px;width:200px;text-align:center"><strong>Member Name</strong>Job Position</p>
  <p class="copy" style="left:16px;top:150px;width:360px;text-align:center">A short biography of this team member goes here.</p>
</section>

<!-- Row 12 -->
<section class="slide std">
  <h2 class="title">Monthly Subscription</h2>
  <div class="box-dark" style="left:20px;top:50px;width:110px;height:130px"></div>
  <div class="box-red" style="left:141px;top:40px;width:110px;height:150px"></div>
  <div class="box-dark" style="left:262px;top:50px;width:110px;height:130px"></div>
  <div class="stat" style="left:20px;width:110px;text-align:center;top:68px;color:#fff">$30</div>
  <div class="stat" style="left:141px;width:110px;text-align:center;top:62px;color:#fff">$90</div>
  <div class="stat" style="left:262px;width:110px;text-align:center;top:68px;color:#fff">$60</div>
  <div class="box-grey" style="left:20px;top:100px;width:110px;height:80px"></div>
  <div class="box-grey" style="left:141px;top:100px;width:110px;height:90px"></div>
  <div class="box-grey" style="left:262px;top:100px;width:110px;height:80px"></div>
</section>
<section class="slide std">
  <h2 class="title">Your Title Goes Here</h2>
  <svg style="left:16px;top:40px" width="360" height="150" viewBox="0 0 360 150">
    <rect width="360" height="18" fill="#2a2a2d"/><rect x="0" width="90" height="18" fill="#e3262d"/>
    <g fill="#ececed"><rect y="36" width="360" height="18"/><rect y="72" width="360" height="18"/><rect y="108" width="360" height="18"/></g>
    <g font-family="Open Sans" font-size="5" fill="#6b6b70">
      <text x="8" y="30">Item</text><text x="98" y="30">Value</text><text x="188" y="30">Value</text><text x="278" y="30">Value</text>
      <text x="8" y="48">Item</text><text x="98" y="48">Value</text><text x="188" y="48">Value</text><text x="278" y="48">Value</text>
      <text x="8" y="66">Item</text><text x="98" y="66">Value</text><text x="188" y="66">Value</text><text x="278" y="66">Value</text>
      <text x="8" y="84">Item</text><text x="98" y="84">Value</text><text x="188" y="84">Value</text><text x="278" y="84">Value</text>
    </g>
    <g font-family="Montserrat" font-size="5.5" font-weight="700" fill="#fff"><text x="8" y="12">Header</text><text x="98" y="12">Header</text><text x="188" y="12">Header</text><text x="278" y="12">Header</text></g>
  </svg>
</section>
<section class="slide std">
  <h2 class="title">Our Team</h2>
  <div class="photo office round" role="img" aria-label="Team member portrait" style="left:30px;top:50px;width:40px;height:40px"></div>
  <div class="photo office round" role="img" aria-label="Team member portrait" style="left:210px;top:50px;width:40px;height:40px"></div>
  <div class="photo office round" role="img" aria-label="Team member portrait" style="left:30px;top:120px;width:40px;height:40px"></div>
  <div class="photo office round" role="img" aria-label="Team member portrait" style="left:210px;top:120px;width:40px;height:40px"></div>
  <p class="copy" style="left:78px;top:56px;width:110px"><strong>Member Name</strong>Job Position</p>
  <p class="copy" style="left:258px;top:56px;width:110px"><strong>Member Name</strong>Job Position</p>
  <p class="copy" style="left:78px;top:126px;width:110px"><strong>Member Name</strong>Job Position</p>
  <p class="copy" style="left:258px;top:126px;width:110px"><strong>Member Name</strong>Job Position</p>
</section>

<!-- Row 13 -->
<section class="slide std">
  <h2 class="title">Customer Testimonials</h2>
  <div class="photo office round" role="img" aria-label="Customer portrait" style="left:30px;top:50px;width:50px;height:50px"></div>
  <p class="copy" style="left:96px;top:54px;width:270px">“A short testimonial quote from a happy customer goes here.”</p>
  <div class="box-dark" style="left:0;top:140px;width:392px;height:81px"></div>
  <p class="copy" style="left:30px;top:160px;width:330px"><strong>Customer Name</strong>Company Position</p>
</section>
<section class="slide std">
  <h2 class="title">Two Pictures Slide</h2>
  <div class="photo sky" role="img" aria-label="Sunrise over the sea" style="left:16px;top:40px;width:175px;height:120px"></div>
  <div class="photo sunset" role="img" aria-label="Airliner against an orange sky" style="left:201px;top:40px;width:175px;height:120px"></div>
  <p class="copy" style="left:16px;top:168px;width:175px">Short caption for the first picture</p>
  <p class="copy" style="left:201px;top:168px;width:175px">Short caption for the second picture</p>
</section>
<section class="slide std">
  <h2 class="title">Title and Image + Text</h2>
  <div class="photo beach" role="img" aria-label="People running on a beach" style="left:16px;top:40px;width:200px;height:130px"></div>
  <p class="copy" style="left:230px;top:44px;width:146px"><strong>Your Title Here</strong>Add a short paragraph of supporting text here.</p>
</section>

<!-- Row 14 -->
<section class="slide std">
  <h2 class="title">Sales Comparison</h2>
  <svg style="left:16px;top:40px" width="170" height="100" viewBox="0 0 170 100">
    <g fill="#2a2a2d"><rect x="10" y="40" width="14" height="60"/><rect x="40" y="20" width="14" height="80"/><rect x="70" y="50" width="14" height="50"/><rect x="100" y="30" width="14" height="70"/></g>
  </svg>
  <svg style="left:206px;top:40px" width="170" height="100" viewBox="0 0 170 100">
    <g fill="#e3262d"><rect x="10" y="30" width="14" height="70"/><rect x="40" y="10" width="14" height="90"/><rect x="70" y="40" width="14" height="60"/><rect x="100" y="20" width="14" height="80"/></g>
  </svg>
  <div class="stat" style="left:26px;top:150px">45%</div>
  <div class="stat" style="left:216px;top:150px;color:var(--red)">68%</div>
</section>
<section class="slide std">
  <div class="photo city" role="img" aria-label="Grey office background" style="left:0;top:0;width:392px;height:90px"></div>
  <h2 class="title" style="left:0;width:392px;text-align:center;top:34px;color:#fff">Your Title Goes Here</h2>
  <div class="box-dark" style="left:16px;top:100px;width:115px;height:80px"></div>
  <div class="box-red" style="left:138px;top:100px;width:115px;height:80px"></div>
  <div class="box-dark" style="left:260px;top:100px;width:116px;height:80px"></div>
  <p class="copy" style="left:24px;top:112px;width:100px"><strong>Heading</strong>Short text here</p>
  <p class="copy on-red" style="left:146px;top:112px;width:100px"><strong>Heading</strong>Short text here</p>
  <p class="copy" style="left:268px;top:112px;width:100px"><strong>Heading</strong>Short text here</p>
</section>
<section class="slide std">
  <div style="left:0;top:0;width:392px;height:70px;background:#1a1a1c"></div>
  <div class="logo light" style="left:20px;top:16px">PALOMAR VISTA</div>
  <h2 style="left:20px;top:40px;color:#fff;font-size:10px;font-weight:700">This is Your Timeline Page</h2>
  <div style="left:20px;top:140px;width:352px;height:1px;background:var(--silver)"></div>
  <div style="left:50px;top:136px;width:9px;height:9px;border-radius:50%;background:var(--red)"></div>
  <div style="left:150px;top:136px;width:9px;height:9px;border-radius:50%;background:var(--char)"></div>
  <div style="left:250px;top:136px;width:9px;height:9px;border-radius:50%;background:var(--red)"></div>
  <div style="left:340px;top:136px;width:9px;height:9px;border-radius:50%;background:var(--char)"></div>
  <p class="copy" style="left:36px;top:112px">Year 2015</p><p class="copy" style="left:136px;top:152px">Year 2016</p><p class="copy" style="left:236px;top:112px">Year 2017</p><p class="copy" style="left:322px;top:152px">Year 2018</p>
</section>

<!-- Row 15 -->
<section class="slide std">
  <h2 class="title">Your Title</h2>
  <div class="photo office" role="img" aria-label="Laptop on a desk" style="left:170px;top:0;width:222px;height:110px"></div>
  <div class="list" style="left:16px;top:50px;width:140px">
    <div class="item"><i></i><p class="copy">Your text here</p></div>
    <div class="item"><i class="k"></i><p class="copy">Your text here</p></div>
  </div>
  <p class="copy" style="left:170px;top:125px;width:200px">Add a short paragraph of supporting text here.</p>
</section>
<section class="slide std">
  <h2 class="title">Your Title</h2>
  <div class="photo office" role="img" aria-label="Person working on a laptop" style="left:196px;top:0;width:196px;height:110px"></div>
  <div class="list" style="left:16px;top:46px;width:160px">
    <div class="item"><i></i><p class="copy">Your text here</p></div>
    <div class="item"><i class="k"></i><p class="copy">Your text here</p></div>
  </div>
  <div class="box-red" style="left:196px;top:110px;width:196px;height:111px"></div>
  <p class="copy on-red" style="left:210px;top:126px;width:170px"><strong>Heading Here</strong>Short supporting text here.</p>
</section>
<section class="slide std">
  <svg style="left:40px;top:40px" width="110" height="110" viewBox="0 0 110 110">
    <circle cx="55" cy="55" r="42" fill="none" stroke="#ececed" stroke-width="14"/>
    <circle cx="55" cy="55" r="42" fill="none" stroke="#e3262d" stroke-width="14" stroke-dasharray="224 264" transform="rotate(-90 55 55)"/>
    <text x="55" y="60" text-anchor="middle" font-family="Montserrat" font-weight="700" font-size="15" fill="#1d1d1f">85%</text>
  </svg>
  <div class="list" style="left:200px;top:50px;width:170px">
    <div class="item"><i></i><p class="copy">Your text here</p></div>
    <div class="item"><i class="k"></i><p class="copy">Your text here</p></div>
    <div class="item"><i></i><p class="copy">Your text here</p></div>
  </div>
</section>

<!-- Row 16 -->
<section class="slide std">
  <h2 class="title">Who We Are?</h2>
  <div class="list" style="left:16px;top:46px;width:160px">
    <div class="item"><i></i><p class="copy" style="color:var(--red)">A Title About Contents</p></div>
    <div class="item"><i></i><p class="copy" style="color:var(--red)">A Title About Contents</p></div>
    <div class="item"><i></i><p class="copy" style="color:var(--red)">A Title About Contents</p></div>
  </div>
  <div class="photo mono" role="img" aria-label="Office building" style="left:206px;top:30px;width:170px;height:160px"></div>
</section>
<section class="slide std">
  <h2 class="title">Bullet &amp; Chart Area</h2>
  <svg style="left:30px;top:50px" width="110" height="110" viewBox="-55 -55 110 110">
    <circle r="50" fill="#c9c9cc"/>
    <path d="M0 0L0-50A50 50 0 0 1 47 17z" fill="#2a2a2d"/>
    <path d="M0 0L47 17A50 50 0 0 1-20 46z" fill="#e3262d"/>
  </svg>
  <div class="list" style="left:200px;top:50px;width:170px">
    <div class="item"><i></i><p class="copy">Your text here</p></div>
    <div class="item"><i class="k"></i><p class="copy">Your text here</p></div>
    <div class="item"><i class="g"></i><p class="copy">Your text here</p></div>
  </div>
</section>
<section class="slide std">
  <svg style="left:60px;top:70px" width="80" height="80" viewBox="0 0 80 80">
    <circle cx="40" cy="40" r="32" fill="none" stroke="#2a2a2d" stroke-width="10"/>
    <circle cx="40" cy="40" r="32" fill="none" stroke="#e3262d" stroke-width="10" stroke-dasharray="117 201" transform="rotate(-90 40 40)"/>
    <text x="40" y="45" text-anchor="middle" font-family="Montserrat" font-weight="700" font-size="13" fill="#e3262d">58%</text>
  </svg>
  <h2 class="hero" style="left:220px;top:40px;font-size:11px;text-transform:none">Your Title<br>Here</h2>
  <p class="copy" style="left:220px;top:80px;width:150px">Add a short paragraph of supporting text here.</p>
</section>

<!-- Row 17 -->
<section class="slide std">
  <h2 class="title">Bullet &amp; Chart Area</h2>
  <svg style="left:16px;top:44px" width="190" height="130" viewBox="0 0 190 130">
    <g fill="#e3262d"><rect y="0" width="150" height="10"/><rect y="36" width="110" height="10"/><rect y="72" width="170" height="10"/><rect y="108" width="90" height="10"/></g>
    <g fill="#2a2a2d"><rect y="12" width="100" height="10"/><rect y="48" width="140" height="10"/><rect y="84" width="70" height="10"/><rect y="120" width="120" height="10"/></g>
  </svg>
  <div class="list" style="left:230px;top:50px;width:146px">
    <div class="item"><i></i><p class="copy">Your text here</p></div>
    <div class="item"><i class="k"></i><p class="copy">Your text here</p></div>
    <div class="item"><i></i><p class="copy">Your text here</p></div>
  </div>
</section>
<section class="slide std">
  <h2 class="title">Bullet &amp; Chart Area</h2>
  <div class="list" style="left:16px;top:50px;width:140px">
    <div class="item"><i></i><p class="copy">Your text here</p></div>
    <div class="item"><i class="k"></i><p class="copy">Your text here</p></div>
    <div class="item"><i></i><p class="copy">Your text here</p></div>
  </div>
  <svg style="left:170px;top:50px" width="206" height="130" viewBox="0 0 206 130">
    <g fill="#e3262d"><rect x="10" y="40" width="14" height="90"/><rect x="60" y="20" width="14" height="110"/><rect x="110" y="60" width="14" height="70"/><rect x="160" y="30" width="14" height="100"/></g>
    <g fill="#8c8c90"><rect x="26" y="70" width="14" height="60"/><rect x="76" y="50" width="14" height="80"/><rect x="126" y="40" width="14" height="90"/><rect x="176" y="80" width="14" height="50"/></g>
  </svg>
</section>
<section class="slide std">
  <h2 class="title">Column Chart</h2>
  <svg style="left:16px;top:40px" width="360" height="150" viewBox="0 0 360 150">
    <g stroke="#ececed"><line x1="0" y1="30" x2="360" y2="30"/><line x1="0" y1="70" x2="360" y2="70"/><line x1="0" y1="110" x2="360" y2="110"/></g>
    <g fill="#2a2a2d"><rect x="20" y="40" width="22" height="110"/><rect x="110" y="60" width="22" height="90"/><rect x="200" y="30" width="22" height="120"/><rect x="290" y="70" width="22" height="80"/></g>
    <g fill="#e3262d"><rect x="46" y="20" width="22" height="130"/><rect x="136" y="80" width="22" height="70"/><rect x="226" y="50" width="22" height="100"/><rect x="316" y="40" width="22" height="110"/></g>
  </svg>
</section>

<!-- Row 18 -->
<section class="slide std">
  <h2 class="title">Production Steps</h2>
  <div class="box-dark" style="left:0;top:90px;width:392px;height:131px"></div>
  <div class="num box-red" style="left:20px;top:50px;width:80px;height:60px;font-size:22px">1</div>
  <div class="photo office" role="img" aria-label="Production workspace" style="left:110px;top:50px;width:80px;height:60px"></div>
  <div class="photo city" role="img" aria-label="Team collaborating" style="left:200px;top:50px;width:80px;height:60px"></div>
  <div class="photo mono" role="img" aria-label="Finished product" style="left:290px;top:50px;width:80px;height:60px"></div>
  <p class="copy" style="left:20px;top:130px;width:80px"><strong>Step One</strong>Short text</p>
  <p class="copy" style="left:110px;top:130px;width:80px"><strong>Step Two</strong>Short text</p>
  <p class="copy" style="left:200px;top:130px;width:80px"><strong>Step Three</strong>Short text</p>
  <p class="copy" style="left:290px;top:130px;width:80px"><strong>Step Four</strong>Short text</p>
</section>
<section class="slide std">
  <h2 class="title">Three Steps</h2>
  <div class="list" style="left:16px;top:50px;width:160px">
    <div class="item"><i></i><p class="copy"><strong>Step One</strong>Short text here</p></div>
    <div class="item"><i class="k"></i><p class="copy"><strong>Step Two</strong>Short text here</p></div>
    <div class="item"><i class="g"></i><p class="copy"><strong>Step Three</strong>Short text here</p></div>
  </div>
  <svg style="left:230px;top:30px" width="120" height="170" viewBox="0 0 120 170">
    <g fill="none" stroke-width="14">
      <circle cx="60" cy="32" r="24" stroke="#e3262d"/>
      <circle cx="60" cy="85" r="24" stroke="#2a2a2d"/>
      <circle cx="60" cy="138" r="24" stroke="#8c8c90"/>
    </g>
  </svg>
</section>
<section class="slide std">
  <h2 class="title">Project Timeline</h2>
  <svg style="left:16px;top:40px" width="360" height="150" viewBox="0 0 360 150">
    <rect width="360" height="14" fill="#2a2a2d"/>
    <g stroke="#ececed"><line x1="90" y1="14" x2="90" y2="150"/><line x1="180" y1="14" x2="180" y2="150"/><line x1="270" y1="14" x2="270" y2="150"/></g>
    <rect x="60" y="26" width="90" height="10" fill="#e3262d"/>
    <rect x="100" y="50" width="110" height="10" fill="#8c8c90"/>
    <rect x="150" y="74" width="80" height="10" fill="#e3262d"/>
    <rect x="200" y="98" width="120" height="10" fill="#8c8c90"/>
    <rect x="260" y="122" width="90" height="10" fill="#e3262d"/>
    <g font-family="Open Sans" font-size="5" fill="#6b6b70"><text x="4" y="34">Task One</text><text x="4" y="58">Task Two</text><text x="4" y="82">Task Three</text><text x="4" y="106">Task Four</text><text x="4" y="130">Task Five</text></g>
  </svg>
</section>

<!-- Row 19 -->
<section class="slide std">
  <div class="photo office" role="img" aria-label="Notebook and pen on a desk" style="left:0;top:0;width:170px;height:221px"></div>
  <div class="box-dark" style="left:170px;top:0;width:222px;height:221px"></div>
  <h2 class="title" style="left:186px;top:40px;color:#fff">Key Points</h2>
  <div class="list" style="left:186px;top:66px;width:180px">
    <div class="item"><i></i><p class="copy">Your key point text here</p></div>
    <div class="item"><i></i><p class="copy">Your key point text here</p></div>
    <div class="item"><i></i><p class="copy">Your key point text here</p></div>
  </div>
</section>
<section class="slide std">
  <h2 class="title">Three Bullets Area</h2>
  <div class="photo office" role="img" aria-label="Colleagues working together" style="left:0;top:40px;width:392px;height:90px"></div>
  <div style="left:60px;top:118px;width:24px;height:24px;border-radius:50%;background:var(--red)"></div>
  <div style="left:184px;top:118px;width:24px;height:24px;border-radius:50%;background:var(--char)"></div>
  <div style="left:308px;top:118px;width:24px;height:24px;border-radius:50%;background:var(--grey)"></div>
  <p class="copy" style="left:22px;top:150px;width:100px;text-align:center"><strong>Heading</strong>Short text</p>
  <p class="copy" style="left:146px;top:150px;width:100px;text-align:center"><strong>Heading</strong>Short text</p>
  <p class="copy" style="left:270px;top:150px;width:100px;text-align:center"><strong>Heading</strong>Short text</p>
</section>
<section class="slide black">
  <div class="photo dusk" role="img" aria-label="Dark office background" style="left:0;top:0;width:392px;height:221px;opacity:.7"></div>
  <h2 class="hero" style="left:20px;top:40px">Thank You</h2>
  <p class="sub" style="left:21px;top:62px">Send your feedback</p>
  <div class="logo light" style="left:260px;top:150px">PALOMAR VISTA</div>
</section>

<!-- Row 20 -->
<section class="slide dark">
  <div class="photo dusk" role="img" aria-label="Dark sky backdrop" style="left:0;top:0;width:392px;height:221px;opacity:.5"></div>
  <div class="logo light" style="left:196px;top:50px">PALOMAR VISTA</div>
  <h2 class="hero" style="left:250px;top:160px;font-size:13px">Extra Slides</h2>
</section>
<section class="slide std">
  <h2 class="title">Org Charts</h2>
  <svg style="left:16px;top:40px" width="360" height="150" viewBox="0 0 360 150">
    <g stroke="#8c8c90" fill="none"><path d="M180 22v16M60 38h240M60 38v14M180 38v14M300 38v14M60 74v14M25 88h70M25 88v12M95 88v12M300 74v14M265 88h70M265 88v12M335 88v12"/></g>
    <rect x="130" width="100" height="22" fill="#e3262d"/>
    <g fill="#2a2a2d"><rect x="20" y="52" width="80" height="22"/><rect x="140" y="52" width="80" height="22"/><rect x="260" y="52" width="80" height="22"/></g>
    <g fill="#ececed"><rect x="0" y="100" width="50" height="20"/><rect x="70" y="100" width="50" height="20"/><rect x="240" y="100" width="50" height="20"/><rect x="310" y="100" width="50" height="20"/></g>
    <g font-family="Montserrat" font-size="5.5" font-weight="700" fill="#fff" text-anchor="middle"><text x="180" y="13">Director</text><text x="60" y="65">Manager</text><text x="180" y="65">Manager</text><text x="300" y="65">Manager</text></g>
    <g font-family="Open Sans" font-size="5" fill="#6b6b70" text-anchor="middle"><text x="25" y="112">Staff</text><text x="95" y="112">Staff</text><text x="265" y="112">Staff</text><text x="335" y="112">Staff</text></g>
  </svg>
</section>
<section class="slide std">
  <h2 class="title">Org Charts</h2>
  <svg style="left:16px;top:40px" width="360" height="150" viewBox="0 0 360 150">
    <g stroke="#8c8c90" fill="none"><path d="M180 20v16M90 36h180M90 36v14M270 36v14M90 70v14M270 70v14"/></g>
    <rect x="120" width="120" height="20" fill="#2a2a2d"/>
    <g fill="#e3262d"><rect x="30" y="50" width="120" height="20"/><rect x="210" y="50" width="120" height="20"/></g>
    <g fill="#ececed"><rect x="30" y="84" width="120" height="36"/><rect x="210" y="84" width="120" height="36"/></g>
    <g font-family="Montserrat" font-size="5.5" font-weight="700" fill="#fff" text-anchor="middle"><text x="180" y="12">Description</text><text x="90" y="62">Description</text><text x="270" y="62">Description</text></g>
    <g font-family="Open Sans" font-size="5" fill="#6b6b70" text-anchor="middle"><text x="90" y="104">Short text here</text><text x="270" y="104">Short text here</text></g>
  </svg>
</section>

<!-- Row 21 -->
<section class="slide std">
  <h2 class="title">Company Structure</h2>
  <svg style="left:16px;top:40px" width="360" height="150" viewBox="0 0 360 150">
    <g stroke="#8c8c90" fill="none"><path d="M180 20v20M40 40h280M40 40v16M140 40v16M220 40v16M320 40v16"/></g>
    <rect x="130" width="100" height="20" fill="#2a2a2d"/>
    <g fill="#2a2a2d"><rect x="10" y="56" width="60" height="18"/><rect x="110" y="56" width="60" height="18"/><rect x="190" y="56" width="60" height="18"/><rect x="290" y="56" width="60" height="18"/></g>
    <g font-family="Open Sans" font-size="5" fill="#fff" text-anchor="middle"><text x="180" y="12">Head Office</text><text x="40" y="67">Division</text><text x="140" y="67">Division</text><text x="220" y="67">Division</text><text x="320" y="67">Division</text></g>
  </svg>
</section>
<section class="slide std">
  <h2 class="title">Plane Infographic</h2>
  <div class="photo mono" role="img" aria-label="Side-view airliner infographic in red, black and grey" style="left:16px;top:40px;width:360px;height:80px;background:linear-gradient(90deg,#3a3a3e,#e3262d 50%,#d6d6d8)"></div>
  <div class="stat" style="left:40px;top:134px">35%</div>
  <div class="stat" style="left:166px;top:134px;color:var(--red)">35%</div>
  <div class="stat" style="left:292px;top:134px">25%</div>
  <p class="copy" style="left:40px;top:156px;width:80px">Short text here</p>
  <p class="copy" style="left:166px;top:156px;width:80px">Short text here</p>
  <p class="copy" style="left:292px;top:156px;width:80px">Short text here</p>
</section>
<section class="slide std">
  <h2 class="title">Plane Infographic</h2>
  <div class="photo mono" role="img" aria-label="Top-view airliner infographic with country flags" style="left:110px;top:40px;width:172px;height:150px"></div>
  <p class="copy" style="left:16px;top:60px;width:84px"><strong>Heading</strong>Short text here</p>
  <p class="copy" style="left:16px;top:120px;width:84px"><strong>Heading</strong>Short text here</p>
  <p class="copy" style="left:292px;top:60px;width:84px"><strong>Heading</strong>Short text here</p>
  <p class="copy" style="left:292px;top:120px;width:84px"><strong>Heading</strong>Short text here</p>
</section>

<!-- Row 22 -->
<section class="slide std">
  <h2 class="title">Bus Infographic</h2>
  <div class="photo mono" role="img" aria-label="Red and black bus infographic" style="left:16px;top:40px;width:170px;height:150px;background:linear-gradient(160deg,#3a3a3e,#e3262d)"></div>
  <div class="list" style="left:206px;top:50px;width:170px">
    <div class="item"><i></i><p class="copy"><strong>Heading</strong>Short text here</p></div>
    <div class="item"><i class="k"></i><p class="copy"><strong>Heading</strong>Short text here</p></div>
    <div class="item"><i class="g"></i><p class="copy"><strong>Heading</strong>Short text here</p></div>
  </div>
</section>
<section class="slide std">
  <h2 class="title">Car Infographic</h2>
  <div class="photo mono" role="img" aria-label="Red, black and grey car infographic" style="left:16px;top:40px;width:170px;height:150px;background:linear-gradient(150deg,#e3262d,#3a3a3e 60%,#c9c9cc)"></div>
  <div class="stat" style="left:206px;top:52px;color:var(--red)">975</div>
  <div class="stat" style="left:206px;top:97px">1,089</div>
  <div class="stat" style="left:206px;top:142px;color:var(--grey)">1,257</div>
  <p class="copy" style="left:270px;top:54px;width:106px">Short text here</p>
  <p class="copy" style="left:270px;top:99px;width:106px">Short text here</p>
  <p class="copy" style="left:270px;top:144px;width:106px">Short text here</p>
</section>
<section class="slide std">
  <h2 class="title">Plane Infographic</h2>
  <div class="photo mono" role="img" aria-label="Three airliners climbing with red, black and grey trails" style="left:226px;top:30px;width:150px;height:170px;background:linear-gradient(180deg,#3a3a3e,#c9c9cc 50%,#e3262d)"></div>
  <div class="stat" style="left:170px;top:62px;color:var(--red)">65%</div>
  <div class="stat" style="left:170px;top:112px">85%</div>
  <p class="copy" style="left:16px;top:60px;width:140px"><strong>Heading Here</strong>Short text here</p>
  <p class="copy" style="left:16px;top:110px;width:140px"><strong>Heading Here</strong>Short text here</p>
</section>

</main>
</body>
</html>
```